k eLiquid Label

We are an electronic cigarette eLiquid manufacturer with an outdated label design which needs to be updated and become more modern. All information listed on the label cannot be changed or removed.

There are 4 colour coding on the labels that cannot change.
0mg is white
12mg is yellow
18mg is blue
24mg is red

We prefer a blue type background however are not committed to it with the proper design however if a new colour is chosen it must compliment the colour band for each colour coding

The "dots" on the front of the bottle need to be larger.

The "V" on the front needs to be in this font however we can accept slight changes to it for effect.

Issues we are facing:
The 0mg and the 18mg look too close in colour and need to be completely different in colouring.

The background colouring is too dark and you cannot see the 50/50 in the watermark.

Reason: We have not received a design which is suitable to our needs. We have see a few close ones however not exact. Thanks

Reason: I was forced to go out of country for a family emergency and to be fair I am extending the deadline

```html
<!DOCTYPE html>
<html lang="en">
<head>
<meta charset="utf-8">
<title>k eLiquid Sweet Tobacco Labels</title>
<link href="https://fonts.googleapis.com/css2?family=PT+Sans+Narrow:wght@400;700&family=Roboto+Slab:wght@700;800&display=swap" rel="stylesheet">
<style>
  :root{
    --page-top:#6f97d6;
    --page-bottom:#c3d4ef;
    --label-dark:#1565c8;
    --label-light:#2f93ea;
    --shield-fill:rgba(38,72,170,.88);
    --watermark:rgba(120,200,245,.55);
    --ink:#0b1533;
    --white:#ffffff;
    --warn:#f5d90a;
    --band-zero:#ffffff;
    --band-12:#f4e21c;
    --band-18:#232c7c;
    --band-24:#e5232b;
  }
  *{box-sizing:border-box;margin:0;padding:0}
  html,body{width:1200px;height:1000px;overflow:hidden}
  body{
    background:linear-gradient(160deg,var(--page-top),var(--page-bottom));
    font-family:"PT Sans Narrow",sans-serif;
    position:relative;
  }
  .label{
    position:absolute;left:40px;width:700px;height:237px;
    background:
      radial-gradient(ellipse 260px 60px at 560px 60px,rgba(255,255,255,.12),transparent 70%),
      radial-gradient(ellipse 300px 50px at 160px 190px,rgba(255,255,255,.1),transparent 70%),
      linear-gradient(180deg,var(--label-light),var(--label-dark));
    box-shadow:0 3px 6px rgba(0,0,0,.35);
    overflow:hidden;color:var(--ink);
  }
  .label--zero{top:5px;--band:var(--band-zero)}
  .label--12{top:253px;--band:var(--band-12)}
  .label--18{top:500px;--band:var(--band-18)}
  .label--24{top:747px;--band:var(--band-24)}

  .copy-fr{
    position:absolute;left:10px;top:11px;width:218px;
    text-align:right;font-size:12.6px;line-height:15.4px;
  }
  .copy-en{
    position:absolute;left:463px;top:11px;width:230px;
    font-size:12.6px;line-height:15.4px;
  }
  .copy-fr b,.copy-en b{font-weight:700}
  .gap{display:block;height:6px}

  .watermark{
    position:absolute;left:240px;top:-8px;width:230px;
    font-family:"PT Sans Narrow",sans-serif;font-weight:700;
    font-size:92px;line-height:84px;color:var(--watermark);
    letter-spacing:-2px;text-align:center;
  }
  .shield{position:absolute;left:242px;top:0;width:226px;height:237px}
  .brand{
    position:absolute;left:242px;top:48px;width:226px;text-align:center;
    font-family:"PT Sans Narrow",sans-serif;font-weight:700;
    font-size:42px;color:var(--white);
  }
  .flavour{
    position:absolute;left:242px;top:145px;width:226px;text-align:center;
    font-family:"Roboto Slab",serif;font-weight:800;font-size:16px;color:var(--white);
  }
  .band{position:absolute;left:0;right:0;top:198px;height:4px;background:var(--band)}
  .nicotine{position:absolute;left:330px;top:172px;width:50px;height:50px}

  .batch{
    position:absolute;left:463px;top:170px;width:232px;height:24px;
    background:var(--white);font-size:12.6px;font-weight:700;
    padding:4px 6px;display:flex;gap:80px;
  }
  .warn-icon{position:absolute;left:652px;top:9px;width:24px;height:22px}

  .footer{
    position:absolute;top:208px;font-size:12.4px;line-height:14px;color:var(--white);
  }
  .footer--fr{left:40px;text-align:left}
  .footer--en{left:463px}
  .volume{
    position:absolute;left:402px;top:212px;font-size:17px;font-weight:700;color:var(--white);
  }
</style>
</head>
<body>

<!-- Label template repeated for each nicotine strength -->
<section class="label label--zero" aria-label="Sweet Tobacco label, zero nicotine">
  <div class="copy-fr">
    <b>CONTENIR NOCIF</b><br>Ne pas avaler.<br>Ne pas mettre dans les yeux ou sur la peau ou les vêtements.<span class="gap"></span>
    Tenir hors de portée des enfants et des animaux.<br><b>INGRÉDIENTS:</b> Propylène Glycol, Glycérine, Alcool de Qualité Alimentaire, Arômes Naturel et Artificiels.<span class="gap"></span>
    <b>En cas d'ingestion consulter centre antipoison ou un medécin immédiatement. Peux contenir de noix.</b>
  </div>
  <div class="watermark" aria-hidden="true">50/50<br>50/50<br>50/50</div>
  <svg class="shield" viewBox="0 0 226 237" aria-hidden="true"><path d="M14 4 H212 Q220 4 218 14 L190 170 Q113 222 36 170 L8 14 Q6 4 14 4Z" fill="var(--shield-fill)" stroke="var(--band)" stroke-width="4"/></svg>
  <div class="brand">k eLiquid</div>
  <div class="flavour">SWEET TOBACCO</div>
  <div class="band"></div>
  <svg class="nicotine" viewBox="0 0 50 50" aria-label="Nicotine zero"><circle cx="25" cy="25" r="22" fill="#2a3f9e" stroke="var(--band)" stroke-width="3"/><text x="25" y="15" font-size="5" fill="#ffffff" text-anchor="middle" font-family="PT Sans Narrow,sans-serif">NICOTINE (mg/ml)</text><text x="25" y="32" font-size="13" font-weight="700" fill="var(--band)" text-anchor="middle" font-family="PT Sans Narrow,sans-serif">ZERO</text></svg>
  <div class="copy-en">
    <b>WARNING CONTENTS HARMFUL</b><br>Do not swallow.<br>Do not get in eyes or on skin or clothing.<br>Keep out of reach of children and pets.<br><b>IN GREDIENTS:</b> Propylene Glycol, Vegetable Glycerin, Food Grade Alcohol, Natural and Artificial Flavours.<br><b>If swallowed consult poison control centre or a doctor immediately.<br>May contain nuts.</b>
  </div>
  <svg class="warn-icon" viewBox="0 0 24 22" aria-label="Hazard"><path d="M12 1 L23 21 H1Z" fill="var(--warn)" stroke="#000" stroke-width="1.5"/><circle cx="12" cy="13" r="3.5" fill="#000"/></svg>
  <div class="batch"><span>BATCH :</span><span>EXPIRES :</span></div>
  <div class="footer footer--fr">Produit et emballlé exclusivement pour:<br>4471920 Canada Inc, Millbrook ON, K0L 1B0</div>
  <div class="volume">30 ml</div>
  <div class="footer footer--en">Produced and Packaged exclusively for :<br>4471920 Canada Inc, Millbrook ON, K0L 1B0</div>
</section>

<section class="label label--12" aria-label="Sweet Tobacco label, 12 mg nicotine">
  <div class="copy-fr">
    <b>CONTENIR NOCIF</b><br>Ne pas avaler.<br>Ne pas mettre dans les yeux ou sur la peau ou les vêtements.<span class="gap"></span>
    Tenir hors de portée des enfants et des animaux.<br><b>INGRÉDIENTS:</b> Propylène Glycol, Glycérine, Alcool de Qualité Alimentaire, Arômes Naturel et Artificiels.<span class="gap"></span>
    <b>En cas d'ingestion consulter centre antipoison ou un medécin immédiatement. Peux contenir de noix.</b>
  </div>
  <div class="watermark" aria-hidden="true">50/50<br>50/50<br>50/50</div>
  <svg class="shield" viewBox="0 0 226 237" aria-hidden="true"><path d="M14 4 H212 Q220 4 218 14 L190 170 Q113 222 36 170 L8 14 Q6 4 14 4Z" fill="var(--shield-fill)" stroke="var(--band)" stroke-width="4"/></svg>
  <div class="brand">k eLiquid</div>
  <div class="flavour">SWEET TOBACCO</div>
  <div class="band"></div>
  <svg class="nicotine" viewBox="0 0 50 50" aria-label="Nicotine 12"><circle cx="25" cy="25" r="22" fill="#2a3f9e" stroke="var(--band)" stroke-width="3"/><text x="25" y="15" font-size="5" fill="#ffffff" text-anchor="middle" font-family="PT Sans Narrow,sans-serif">NICOTINE (mg/ml)</text><text x="25" y="34" font-size="17" font-weight="700" fill="var(--band)" text-anchor="middle" font-family="PT Sans Narrow,sans-serif">12</text></svg>
  <div class="copy-en">
    <b>WARNING CONTENTS HARMFUL</b><br>Do not swallow.<br>Do not get in eyes or on skin or clothing.<br>Keep out of reach of children and pets.<br><b>IN GREDIENTS:</b> Propylene Glycol, Vegetable Glycerin, Food Grade Alcohol, Natural and Artificial Flavours.<br><b>If swallowed consult poison control centre or a doctor immediately.<br>May contain nuts.</b>
  </div>
  <svg class="warn-icon" viewBox="0 0 24 22" aria-label="Hazard"><path d="M12 1 L23 21 H1Z" fill="var(--warn)" stroke="#000" stroke-width="1.5"/><circle cx="12" cy="13" r="3.5" fill="#000"/></svg>
  <div class="batch"><span>BATCH :</span><span>EXPIRES :</span></div>
  <div class="footer footer--fr">Produit et emballlé exclusivement pour:<br>4471920 Canada Inc, Millbrook ON, K0L 1B0</div>
  <div class="volume">30 ml</div>
  <div class="footer footer--en">Produced and Packaged exclusively for :<br>4471920 Canada Inc, Millbrook ON, K0L 1B0</div>
</section>

<section class="label label--18" aria-label="Sweet Tobacco label, 18 mg nicotine">
  <div class="copy-fr">
    <b>CONTENIR NOCIF</b><br>Ne pas avaler.<br>Ne pas mettre dans les yeux ou sur la peau ou les vêtements.<span class="gap"></span>
    Tenir hors de portée des enfants et des animaux.<br><b>INGRÉDIENTS:</b> Propylène Glycol, Glycérine, Alcool de Qualité Alimentaire, Arômes Naturel et Artificiels.<span class="gap"></span>
    <b>En cas d'ingestion consulter centre antipoison ou un medécin immédiatement. Peux contenir de noix.</b>
  </div>
  <div class="watermark" aria-hidden="true">50/50<br>50/50<br>50/50</div>
  <svg class="shield" viewBox="0 0 226 237" aria-hidden="true"><path d="M14 4 H212 Q220 4 218 14 L190 170 Q113 222 36 170 L8 14 Q6 4 14 4Z" fill="var(--shield-fill)" stroke="var(--band)" stroke-width="4"/></svg>
  <div class="brand">k eLiquid</div>
  <div class="flavour">SWEET TOBACCO</div>
  <div class="band"></div>
  <svg class="nicotine" viewBox="0 0 50 50" aria-label="Nicotine 18"><circle cx="25" cy="25" r="22" fill="#2a3f9e" stroke="var(--band)" stroke-width="3"/><text x="25" y="15" font-size="5" fill="#ffffff" text-anchor="middle" font-family="PT Sans Narrow,sans-serif">NICOTINE (mg/ml)</text><text x="25" y="34" font-size="17" font-weight="700" fill="#121a4f" text-anchor="middle" font-family="PT Sans Narrow,sans-serif">18</text></svg>
  <div class="copy-en">
    <b>WARNING CONTENTS HARMFUL</b><br>Do not swallow.<br>Do not get in eyes or on skin or clothing.<br>Keep out of reach of children and pets.<br><b>IN GREDIENTS:</b> Propylene Glycol, Vegetable Glycerin, Food Grade Alcohol, Natural and Artificial Flavours.<br><b>If swallowed consult poison control centre or a doctor immediately.<br>May contain nuts.</b>
  </div>
  <svg class="warn-icon" viewBox="0 0 24 22" aria-label="Hazard"><path d="M12 1 L23 21 H1Z" fill="var(--warn)" stroke="#000" stroke-width="1.5"/><circle cx="12" cy="13" r="3.5" fill="#000"/></svg>
  <div class="batch"><span>BATCH :</span><span>EXPIRES :</span></div>
  <div class="footer footer--fr">Produit et emballlé exclusivement pour:<br>4471920 Canada Inc, Millbrook ON, K0L 1B0</div>
  <div class="volume">30 ml</div>
  <div class="footer footer--en">Produced and Packaged exclusively for :<br>4471920 Canada Inc, Millbrook ON, K0L 1B0</div>
</section>

<section class="label label--24" aria-label="Sweet Tobacco label, 24 mg nicotine">
  <div class="copy-fr">
    <b>CONTENIR NOCIF</b><br>Ne pas avaler.<br>Ne pas mettre dans les yeux ou sur la peau ou les vêtements.<span class="gap"></span>
    Tenir hors de portée des enfants et des animaux.<br><b>INGRÉDIENTS:</b> Propylène Glycol, Glycérine, Alcool de Qualité Alimentaire, Arômes Naturel et Artificiels.<span class="gap"></span>
    <b>En cas d'ingestion consulter centre antipoison ou un medécin immédiatement. Peux contenir de noix.</b>
  </div>
  <div class="watermark" aria-hidden="true">50/50<br>50/50<br>50/50</div>
  <svg class="shield" viewBox="0 0 226 237" aria-hidden="true"><path d="M14 4 H212 Q220 4 218 14 L190 170 Q113 222 36 170 L8 14 Q6 4 14 4Z" fill="var(--shield-fill)" stroke="var(--band)" stroke-width="4"/></svg>
  <div class="brand">k eLiquid</div>
  <div class="flavour">SWEET TOBACCO</div>
  <div class="band"></div>
  <svg class="nicotine" viewBox="0 0 50 50" aria-label="Nicotine 24"><circle cx="25" cy="25" r="22" fill="#2a3f9e" stroke="var(--band)" stroke-width="3"/><text x="25" y="15" font-size="5" fill="#ffffff" text-anchor="middle" font-family="PT Sans Narrow,sans-serif">NICOTINE (mg/ml)</text><text x="25" y="34" font-size="17" font-weight="700" fill="var(--band)" text-anchor="middle" font-family="PT Sans Narrow,sans-serif">24</text></svg>
  <div class="copy-en">
    <b>WARNING CONTENTS HARMFUL</b><br>Do not swallow.<br>Do not get in eyes or on skin or clothing.<br>Keep out of reach of children and pets.<br><b>IN GREDIENTS:</b> Propylene Glycol, Vegetable Glycerin, Food Grade Alcohol, Natural and Artificial Flavours.<br><b>If swallowed consult poison control centre or a doctor immediately.<br>May contain nuts.</b>
  </div>
  <svg class="warn-icon" viewBox="0 0 24 22" aria-label="Hazard"><path d="M12 1 L23 21 H1Z" fill="var(--warn)" stroke="#000" stroke-width="1.5"/><circle cx="12" cy="13" r="3.5" fill="#000"/></svg>
  <div class="batch"><span>BATCH :</span><span>EXPIRES :</span></div>
  <div class="footer footer--fr">Produit et emballlé exclusivement pour:<br>4471920 Canada Inc, Millbrook ON, K0L 1B0</div>
  <div class="volume">30 ml</div>
  <div class="footer footer--en">Produced and Packaged exclusively for :<br>4471920 Canada Inc, Millbrook ON, K0L 1B0</div>
</section>

</body>
</html>
```